Full Page Magazine Add for Bulb Recycler

We need ad that to promote our expertise, capabilities and value in industry trade magazines. We want clean, clear look feel to reflect our impact on the environment.

Target Market(s)

Industry -- Electricians -- Environmental Services

Font styles to use
Sans Serif

Colors
eef8f9

Requirements
Must have
• I have included instructions outlining all details of must / haves -- ALSO) there are 4 jpegs of LOOK/FEEL Examples that we like -- as reference -- FILE names are EXAMPLE
Nice to have
• Welcome guidance on helping with logo transition -- we're moving from Hollis Materials -- to Fair by Fernhill -- but for now -- need to display both -- we've just put an IS in between -- but if you have ideas definitely WELCOME

```html
<!DOCTYPE html>
<html lang="en">
<head>
<meta charset="utf-8">
<title>Hollis Materials – The Nation's Largest Bulb Recycler</title>
<link href="https://fonts.googleapis.com/css2?family=Oswald:wght@700&family=Fira+Sans:wght@700&family=Open+Sans:wght@300;400;700&family=Arimo:wght@400&display=swap" rel="stylesheet">
<style>
  :root{
    --blue:#0f4f93;
    --blue-text:#12549b;
    --yellow:#f1e945;
    --panel:#f2f2f4;
    --ink:#111;
    --body:#333;
    --green:#27a84a;
    --rule:#dcdcdf;
    --white:#fff;
  }
  *{margin:0;padding:0;box-sizing:border-box}
  html,body{width:929px;height:1200px;overflow:hidden;background:var(--white)}
  .ad{position:relative;width:929px;height:1200px;background:var(--panel);font-family:"Open Sans",sans-serif}
  .header{position:absolute;left:0;top:0;width:929px;height:197px;background:var(--blue)}
  .headline{position:absolute;left:30px;top:36px;z-index:2;color:var(--white);font-family:"Oswald",sans-serif;font-weight:700;font-size:60px;line-height:67px;letter-spacing:1px;text-transform:uppercase;white-space:nowrap}
  .tagline-band{position:absolute;left:0;top:197px;width:929px;height:110px;background:var(--yellow)}
  .tagline{position:absolute;left:30px;top:14px;font-family:"Fira Sans",sans-serif;font-weight:700;font-size:33px;line-height:42px;color:var(--ink)}
  .truck-photo{position:absolute;left:505px;top:37px;width:375px;height:268px;z-index:1;
    background:linear-gradient(135deg,#ffffff 0%,#e9ecef 55%,#c8ccd2 100%);
    clip-path:polygon(149px 0,375px 18px,375px 179px,355px 203px,285px 268px,15px 268px,0 193px,15px 143px,95px 73px,135px 63px)}
  .intro{position:absolute;left:30px;top:316px;width:420px;color:var(--blue-text);font-family:"Fira Sans",sans-serif;font-weight:700;font-size:23px;line-height:33px}
  .features{position:absolute;left:30px;top:424px;width:402px}
  .feature{height:112px}
  .feature h3{display:flex;align-items:center;gap:8px;font-family:"Fira Sans",sans-serif;font-weight:700;font-size:14.5px;color:var(--blue-text);line-height:20px;margin-bottom:7px}
  .feature h3::after{content:"";flex:1;height:2px;background:var(--rule)}
  .feature p{font-size:13.1px;line-height:17px;color:var(--body);text-align:justify;font-weight:400}
  .divider{position:absolute;left:475px;top:430px;width:1px;height:470px;background:var(--rule)}
  .range{position:absolute;left:523px;top:326px;font-weight:300;font-size:37px;line-height:39px;color:#222;letter-spacing:-.3px}
  .checklist{position:absolute;left:523px;top:436px;list-style:none}
  .checklist li{display:flex;align-items:center;gap:12px;height:38px;font-family:"Arimo",sans-serif;font-size:26px;color:var(--blue-text)}
  .checklist svg{width:21px;height:21px;flex:none}
  .kit-photo{position:absolute;left:483px;top:636px;width:388px;height:296px;border-radius:6px;background:linear-gradient(160deg,#ffffff 0%,#eef1ee 50%,#cfd8cf 100%)}
  .green-rule{position:absolute;left:0;top:951px;width:929px;height:4px;background:var(--green)}
  .contact-bar{position:absolute;left:0;top:955px;width:929px;height:45px;background:var(--blue)}
  .contact{position:absolute;left:345px;top:0;width:525px;text-align:center;line-height:45px;color:var(--white);font-family:"Fira Sans",sans-serif;font-weight:700;font-size:21px}
  .contact strong{font-size:24px;letter-spacing:.5px}
  .footer{position:absolute;left:0;top:1000px;width:929px;height:200px;background:var(--white)}
  .brand-tab{position:absolute;left:0;top:980px;width:334px;height:40px;background:var(--white);border-top-right-radius:26px}
  .brand{position:absolute;left:28px;top:1010px;width:300px}
  .brand-name{display:flex;align-items:center;gap:12px;font-family:"Fira Sans",sans-serif;font-weight:700;color:var(--blue-text)}
  .brand-name .dot{width:60px;height:60px;border-radius:50%;background:var(--blue-text);flex:none}
  .brand-primary{font-size:30px;line-height:34px}
  .brand-is{display:flex;align-items:center;gap:14px;margin-top:14px;font-family:"Fira Sans",sans-serif;font-weight:700;font-size:24px;color:var(--blue-text)}
  .brand-secondary{display:flex;align-items:center;gap:10px;color:var(--green);font-size:27px}
  .brand-secondary .dot{width:40px;height:40px;border-radius:50%;background:var(--green)}
  .photo{position:absolute;top:1001px;height:176px}
  .photo-plant{left:343px;width:164px;background:linear-gradient(180deg,#c9d2dc 0%,#8ea0b5 60%,#3c5a86 100%)}
  .photo-line{left:514px;width:257px;background:linear-gradient(180deg,#b9c0c6 0%,#8e949a 55%,#5b6068 100%)}
  .photo-batteries{left:777px;width:123px;background:linear-gradient(135deg,#6fc3d3 0%,#b85a8c 50%,#9ccc55 100%)}
</style>
</head>
<body>
<main class="ad">
  <header class="header">
    <h1 class="headline">The Nation’s Largest<br>Bulb Recycler</h1>
  </header>
  <section class="tagline-band">
    <h2 class="tagline">Delivering Safe Processing<br>For 25+ Years</h2>
  </section>
  <div class="truck-photo" role="img" aria-label="White box truck with a driver stepping into the cab"></div>

  <h2 class="intro">Protecting the Environment and<br>Assuring Your Compliance</h2>

  <div class="features">
    <div class="feature">
      <h3>Technology</h3>
      <p>Our processing facilities are equipped with the most advanced recycling equipment in the industry. We safely recycle millions of bulbs every year.</p>
    </div>
    <div class="feature">
      <h3>Reclaiming Resources</h3>
      <p>We separate and produce clean glass, plastic and metals. We remove mercury from bulb phosphor powder and produce virgin-quality mercury for use in research. Clean powder is processed for rare earth metals needed in manufacturing.</p>
    </div>
    <div class="feature">
      <h3>Nationwide</h3>
      <p>We provide processing and licensed pick up of hazardous and universal waste by pallet-full or truck load for many of the largest and most well-known companies, institutions and agencies in the country.</p>
    </div>
    <div class="feature">
      <h3>Fast Easy Mail-In Recycling</h3>
      <p>Fair by Fernhill Recycling kits ensure you have what you need when you need to properly manage your small quantity batteries, bulbs, ballasts, exit signs and more. Pre-paid shipping and processing. Kits shipped within 24 hours.</p>
    </div>
    <div class="feature">
      <h3>Egress Safety Solutions</h3>
      <p>In addition to fully-managed retrofit and recycle of tritium exit sign we offer a complete line of energy and maintenance-free phosphorescent exit signs and safety marking.</p>
    </div>
  </div>

  <div class="divider"></div>

  <p class="range">BULBS, BATTERIES,<br>BALLASTS &amp; MORE.</p>
  <ul class="checklist">
    <li><svg viewBox="0 0 20 20"><circle cx="10" cy="10" r="10" fill="#5cb548"/><path d="M5.5 10.3l3 3 6-6.3" fill="none" stroke="#fff" stroke-width="2.4" stroke-linecap="round" stroke-linejoin="round"/></svg>Mercury Devices</li>
    <li><svg viewBox="0 0 20 20"><circle cx="10" cy="10" r="10" fill="#5cb548"/><path d="M5.5 10.3l3 3 6-6.3" fill="none" stroke="#fff" stroke-width="2.4" stroke-linecap="round" stroke-linejoin="round"/></svg>Exit Signs</li>
    <li><svg viewBox="0 0 20 20"><circle cx="10" cy="10" r="10" fill="#5cb548"/><path d="M5.5 10.3l3 3 6-6.3" fill="none" stroke="#fff" stroke-width="2.4" stroke-linecap="round" stroke-linejoin="round"/></svg>Smoke Detectors</li>
    <li><svg viewBox="0 0 20 20"><circle cx="10" cy="10" r="10" fill="#5cb548"/><path d="M5.5 10.3l3 3 6-6.3" fill="none" stroke="#fff" stroke-width="2.4" stroke-linecap="round" stroke-linejoin="round"/></svg>Auto Airbags</li>
    <li><svg viewBox="0 0 20 20"><circle cx="10" cy="10" r="10" fill="#5cb548"/><path d="M5.5 10.3l3 3 6-6.3" fill="none" stroke="#fff" stroke-width="2.4" stroke-linecap="round" stroke-linejoin="round"/></svg>Electronic Waste</li>
  </ul>
  <div class="kit-photo" role="img" aria-label="Mail-in recycle kits: box, bucket, long tube carton with fluorescent lamps and an exit sign"></div>

  <div class="green-rule"></div>
  <div class="footer"></div>
  <div class="contact-bar">
    <p class="contact">For more details Contact us: <strong>555.014.2290</strong></p>
  </div>
  <div class="brand-tab"></div>
  <div class="brand">
    <div class="brand-name brand-primary"><span class="dot"></span>Hollis<br>Materials</div>
    <div class="brand-is">IS
      <span class="brand-secondary"><span class="dot"></span>Fair by Fernhill</span>
    </div>
  </div>
  <div class="photo photo-plant" role="img" aria-label="Worker in protective gear handling lamps at the processing plant"></div>
  <div class="photo photo-line" role="img" aria-label="Workers sorting tubes on the recycling line"></div>
  <div class="photo photo-batteries" role="img" aria-label="Close-up of colourful batteries"></div>
</main>
</body>
</html>
```